Tallowick Limited Business Card

We need a business card for a new company based in Essex, United Kingdom. We develop and manufacture educational games. The business card needs to match the company brand and logo and the colour scheme.
My company makes educational board games to be played by the family or used by teachers
The games are tile based number game

Target Market(s)

Parents, teachers, schools and children

Industry/Entity Type

Games

Contact Information for Business Card

Company Name - Tallowick Limited
Director - Damian Prouse
Registered Office - 3 Marsh Court, 142 Quarry Lane, Brindleford, Essex, CM7 4XR
Phone Number - 07950 000 318
Email - Enquiries@Tallowick.example
Website - www.Tallowick.example
Company Number - 00000000

Font styles to use
Sans Serif

Colors
00a990
ffffff

Requirements
Must have
• Same colour scheme as the attachments - green and white
• Same font style for Tallowick
• Images of the number tiles similar to the attachments
• extra details
• The colour is Cyan - 82 Magenta - 24 Yellow - 44 Black - 2
• I have attached some of the font styles use on my website and alos my LOGO
Nice to have
• Image of the number "1" tag as seen on the website

```html
<!DOCTYPE html>
<html lang="en">
<head>
<meta charset="utf-8">
<title>Tallowick Limited – Business Card</title>
<link rel="stylesheet" href="https://fonts.googleapis.com/css2?family=Open+Sans:wght@400;600;700&display=swap">
<style>
  :root {
    --teal: #17908f;
    --yellow: #ffd200;
    --name-yellow: #f7cf0a;
    --white: #ffffff;
    --grey-text: #4a4a4a;
    --tile-light: #f4f4f4;
    --tile-mid: #dcdcdc;
    --page: #e9e7e3;
  }
  * { box-sizing: border-box; margin: 0; padding: 0; }
  html, body {
    width: 1200px; height: 834px; overflow: hidden;
    background: var(--page);
    font-family: "Open Sans", Arial, sans-serif;
  }
  .card {
    position: absolute; left: 100px; top: 132px;
    width: 1000px; height: 570px;
    background: var(--white);
    box-shadow: 0 6px 20px rgba(0,0,0,.15);
    overflow: hidden;
  }
  .card__header {
    position: absolute; left: 0; top: 0; width: 100%; height: 244px;
    background: var(--teal);
  }
  .brand { position: absolute; left: 58px; top: 50px; color: var(--white); font-weight: 700; }
  .brand__name { font-size: 62px; line-height: 1; letter-spacing: -1px; display: block; }
  .brand__suffix { font-size: 22px; letter-spacing: 9px; display: block; margin: 8px 0 0 62px; font-weight: 600; }
  .person { position: absolute; right: 50px; top: 118px; text-align: right; }
  .person__name { color: var(--name-yellow); font-size: 50px; font-weight: 400; line-height: 1.05; }
  .person__role { color: var(--white); font-size: 24px; letter-spacing: 5px; font-weight: 400; margin-top: 2px; margin-right: -5px; }
  .tiles-visual {
    position: absolute; left: 38px; top: 392px;
    width: 284px; height: 68px; border-radius: 8px;
    background: linear-gradient(90deg, var(--tile-light), var(--tile-mid));
  }
  .contacts { position: absolute; right: 40px; top: 326px; list-style: none; }
  .contacts li {
    display: flex; justify-content: flex-end; align-items: center;
    height: 37px; font-size: 27px; color: var(--grey-text); letter-spacing: .5px;
  }
  .contacts svg { width: 22px; height: 22px; margin-left: 18px; fill: var(--teal); }
  .card__rule { position: absolute; left: 0; top: 488px; width: 100%; height: 6px; background: var(--teal); }
  .card__footer {
    position: absolute; left: 0; top: 494px; width: 100%; height: 76px;
    background: var(--yellow);
    display: flex; align-items: center; justify-content: space-between;
    padding: 0 34px 0 39px;
  }
  .office { color: var(--teal); font-size: 21px; white-space: nowrap; }
  .card__footer svg { width: 24px; height: 30px; fill: var(--teal); }
</style>
</head>
<body>
<main class="card">
  <header class="card__header">
    <div class="brand">
      <span class="brand__name">Tallowick</span>
      <span class="brand__suffix">LIMITED</span>
    </div>
    <div class="person">
      <p class="person__name">Damian Prouse</p>
      <p class="person__role">DIRECTOR</p>
    </div>
  </header>

  <div class="tiles-visual" role="img" aria-label="Row of four number game tiles showing 5, 7, 1 and 2"></div>

  <ul class="contacts">
    <li>00000000
      <svg viewBox="0 0 24 24"><path d="M7 1h10a2 2 0 0 1 2 2v18a2 2 0 0 1-2 2H7a2 2 0 0 1-2-2V3a2 2 0 0 1 2-2zm0 3v14h10V4z"/></svg></li>
    <li>07950 000 318
      <svg viewBox="0 0 24 24"><path d="M6.6 10.8a15.1 15.1 0 0 0 6.6 6.6l2.2-2.2a1 1 0 0 1 1-.25 11.4 11.4 0 0 0 3.6.57 1 1 0 0 1 1 1V20a1 1 0 0 1-1 1A17 17 0 0 1 3 4a1 1 0 0 1 1-1h3.5a1 1 0 0 1 1 1c0 1.25.2 2.45.57 3.57a1 1 0 0 1-.25 1z"/></svg></li>
    <li>www.Tallowick.example
      <svg viewBox="0 0 24 24"><path d="M12 2a10 10 0 1 0 0 20 10 10 0 0 0 0-20zm6.9 6h-3a15.6 15.6 0 0 0-1.4-3.6A8 8 0 0 1 18.9 8zM12 4c.8 1.2 1.5 2.5 1.9 4h-3.8c.4-1.5 1.1-2.8 1.9-4zM4.3 14a8 8 0 0 1 0-4h3.4a16.5 16.5 0 0 0 0 4zm.8 2h3a15.6 15.6 0 0 0 1.4 3.6A8 8 0 0 1 5.1 16zm3-8h-3a8 8 0 0 1 4.4-3.6A15.6 15.6 0 0 0 8.1 8zM12 20c-.8-1.2-1.5-2.5-1.9-4h3.8c-.4 1.5-1.1 2.8-1.9 4zm2.3-6H9.7a14.7 14.7 0 0 1 0-4h4.6a14.7 14.7 0 0 1 0 4zm.3 5.6a15.6 15.6 0 0 0 1.4-3.6h3a8 8 0 0 1-4.4 3.6zm1.7-5.6a16.5 16.5 0 0 0 0-4h3.4a8 8 0 0 1 0 4z"/></svg></li>
    <li>Enquiries@Tallowick.example
      <svg viewBox="0 0 24 24"><path d="M2 5h20v14H2zm2 2v.5l8 5 8-5V7zm0 2.9V17h16V9.9l-8 5z"/></svg></li>
  </ul>

  <div class="card__rule"></div>
  <footer class="card__footer">
    <p class="office">Registered Office - 3 Marsh Court, 142 Quarry Lane, Brindleford, Essex, CM7 4XR</p>
    <svg viewBox="0 0 24 30"><path d="M12 0a11 11 0 0 0-11 11c0 8 11 19 11 19s11-11 11-19A11 11 0 0 0 12 0zm0 15a4 4 0 1 1 0-8 4 4 0 0 1 0 8z"/></svg>
  </footer>
</main>
</body>
</html>
```